Chai Tea Company needs a Tea Packaging Box Design

Tea Packaging
Dimensions of the Tea Packaging Box: Height 13 cm; Width 8.5 cm; Depth 7 cm
Individual Teabag Packet/ Sachet: Width 6.5 cm; Length 8.25 cm
We are looking for a new tea packaging design, for our tea business. The material of the box is cardboard. We are also looking for a design that will be on each individual tea bag sachet/packet that goes into the box. This design will be very similar to what you design for the tea packaging box.
Product Info:
Our tea company is called “Velmora Leaf”. We sell two types of Chai Tea, once called “Velmora Gold” and one called “Velmora Bloom”. The Velmora Gold has caffeine, while the Velmora Bloom is Naturally Caffeine Free. The Velmora Gold has a black tea base, while the Velmora Bloom has a Rooibos tea base. We will need two tea packaging designs, one for each Chai Tea flavour. The designs for both the teas can be similar, but make sure that you can easily distinguish one from the other (example: make them have different colours or pictures). Both the chai teas, come from the same product line.
Tea Packaging Design:
We are looking for high end tea packaging. We produce high quality teas, and we would like to portray this in our tea packaging. Our teas are made with no artificial flavourings, natural flavourings, or preservatives, so we would also like a natural, organic, high quality look to our tea packaging. Our current logo is a llama. It would be great if you could make the current logo more polished and well made. If you feel that the llama is not well suited or you would like to design the llama differently, we are open to your creative ideas.
General Basic Info:
Keep in mind, we will have both English and French writing on the tea packaging. You do not need to worry about the French writing (we will do the translation), just make sure there is room for it. However, if you feel that you are capable and knowledgeable of incorporating both French and English language into the tea packaging that would be of great help and value.
Back of the Box:
- Will have ingredients and brewing instructions. Basic brewing instructions are: “Add hot water to teabag. Steep for 5-7 minutes, depending on strength preferred. Add milk and your choice of sweetener. Enjoy! See inside panel of box for more detailed instructions”. (The basic brewing instructions, can further be polished or written in a more creative or professional manner).
Front of the Box:
- Will have company name, type of tea, little description of the tea
- 18 teabags
- 54 g (1.9 OZ)
- Should state that this is a product of Alberta, Canada.
Side of the Box:
Any creative wording, slogan, or description about the tea, or whatever you feel would be good on the side of the box.
On the inside flap of the side of the box, there will be detailed instructions on how to brew the tea. These will be different from the simplified brewing instructions on the back of the box. I have attached the advanced brewing instructions as a file. These instructions can further be simplified or reduced to make it easier and cleaner for the consumers to read.
Individual Tea Sachets/ Packets
- These will have a matching look and design of the tea box packaging, except on a smaller scale. Each individual sachet will have the company name, type of tea, little description of the tea in the front of the sachet, while the back will contain the ingredients, and basic brewing instructions.
I have attached a few files, with the dimensions, ingredients, detailed brewing directions, and current logo of the business.
If you have any questions, about the design or packaging please let me know. The winning designer will be required to do a few additional tweaks to finalize the product. Thank you for your time and happy designing!

```html
<!DOCTYPE html>
<html lang="en">
<head>
<meta charset="utf-8">
<title>Velmora Leaf – Velmora Gold Tea Box and Sachet</title>
<link rel="stylesheet" href="https://fonts.googleapis.com/css2?family=Marcellus+SC&family=Great+Vibes&display=swap">
<style>
  :root {
    --bg: #e4e3e1;
    --kraft: #a88b5c;
    --kraft-dark: #94784c;
    --label: #f8f7f4;
    --ink: #4b4b4b;
    --ink-soft: #8a8a8a;
    --blue: #7fa2b8;
    --gold: #a98f5b;
    --llama-dark: #2b2622;
    --llama-blue: #a9c6d6;
  }
  * { box-sizing: border-box; margin: 0; padding: 0; }
  html, body { width: 1200px; height: 1000px; overflow: hidden; }
  body {
    background: var(--bg);
    font-family: "Marcellus SC", serif;
    color: var(--ink);
    position: relative;
  }

  /* ---------- shared package shell ---------- */
  .package {
    position: absolute;
    background: linear-gradient(90deg, var(--kraft-dark), var(--kraft) 12%, var(--kraft) 88%, var(--kraft-dark));
    box-shadow: 0 6px 18px rgba(0,0,0,.12);
  }
  .label {
    position: absolute;
    top: 0;
    bottom: 0;
    left: 50%;
    transform: translateX(-50%);
    background: var(--label);
    text-align: center;
    display: flex;
    flex-direction: column;
    align-items: center;
  }
  .brand-name { color: var(--blue); letter-spacing: .5px; line-height: 1.1; }
  .product-name { font-family: "Great Vibes", cursive; font-weight: normal; color: var(--blue); line-height: 1; }
  .variety-row {
    display: flex;
    justify-content: space-between;
    width: 100%;
    color: var(--gold);
    line-height: 1.1;
  }
  .variety-row small { display: block; color: var(--ink-soft); }
  .variety-row .dot { background: var(--ink-soft); }
  .description { line-height: 1.25; width: 100%; border-bottom: 2px solid var(--gold); }
  .description-fr { color: var(--ink-soft); line-height: 1.3; }
  .mascot { display: block; border-radius: 6px; }
  .mascot--dark { background: linear-gradient(180deg, #3b3430, var(--llama-dark)); }
  .mascot--blue { background: linear-gradient(180deg, #c4d8e3, var(--llama-blue)); }
  .heading { color: var(--blue); font-weight: normal; line-height: 1.1; }

  /* ---------- boxes ---------- */
  .box { top: 360px; width: 400px; height: 610px; }
  .box--front { left: 100px; }
  .box--back { left: 700px; }
  .box .label { width: 240px; padding: 20px 16px 18px; }
  .box .variety-row { font-size: 13px; }
  .box .variety-row small { font-size: 8.5px; }
  .box .variety-row .dot { width: 5px; height: 5px; margin-top: 5px; }
  .box .product-name { font-size: 40px; margin-top: 10px; }
  .box .description { font-size: 10px; margin-top: 4px; padding-bottom: 6px; }
  .box .description-fr { font-size: 8.5px; margin-top: 5px; }
  .box .mascot--dark { width: 140px; height: 130px; margin-top: 18px; }
  .box .brand-name { font-size: 24px; margin-top: 12px; }
  .count { font-size: 32px; color: var(--gold); margin-top: 10px; line-height: 1; }
  .count-label { font-size: 13px; color: var(--gold); line-height: 1.1; }
  .count-label small { display: block; font-size: 9.5px; }
  .fine-print { font-size: 8.5px; line-height: 1.4; margin-top: 6px; }
  .fine-print strong { font-weight: normal; font-size: 11px; display: block; }

  .box--back .heading { font-size: 15px; margin-top: 26px; }
  .box--back .heading:first-child { margin-top: 18px; }
  .box--back p { font-size: 10.5px; line-height: 1.45; text-align: left; margin-top: 11px; width: 100%; }
  .box--back p.note { text-align: center; font-size: 8.5px; margin-top: 8px; }
  .box--back p.ingredients { text-align: center; }
  .box--back .mascot--blue { width: 90px; height: 90px; margin-top: auto; }
  .box--back .brand-name { font-size: 21px; margin-top: 8px; }
  .address { font-size: 9.5px; line-height: 1.3; margin-top: 14px; }

  /* ---------- sachets ---------- */
  .sachet { top: 30px; width: 240px; height: 300px; }
  .sachet--front { left: 180px; }
  .sachet--back { left: 780px; }
  .sachet .label { width: 180px; padding: 6px 12px 10px; }
  .tear-line {
    width: 100%;
    border-top: 1px dashed var(--ink-soft);
    font-size: 5.5px;
    text-align: left;
    padding-top: 2px;
    color: var(--ink);
  }
  .sachet .mascot--blue { width: 64px; height: 64px; margin-top: 10px; }
  .sachet--front .brand-name { font-size: 16px; margin-top: 6px; }
  .sachet .variety-row { font-size: 8.5px; margin-top: 10px; }
  .sachet .variety-row small { font-size: 6px; }
  .sachet .variety-row .dot { width: 4px; height: 4px; margin-top: 3px; }
  .sachet .product-name { font-size: 26px; margin-top: 6px; }
  .sachet .description { font-size: 7px; margin-top: 3px; padding-bottom: 4px; border-bottom-width: 1px; }
  .sachet .description-fr { font-size: 6px; margin-top: 3px; }

  .sachet--back .label { padding-top: 12px; }
  .sachet--back .heading { font-size: 9.5px; margin-top: 10px; }
  .sachet--back .heading:first-child { margin-top: 0; }
  .sachet--back p { font-size: 7px; line-height: 1.35; text-align: left; margin-top: 6px; width: 100%; }
  .sachet--back p.note { text-align: center; font-size: 6px; margin-top: 4px; }
  .sachet--back p.ingredients { text-align: center; }
  .sachet--back p.retail { text-align: center; font-size: 7px; margin-top: 8px; }
  .sachet--back .brand-name { font-size: 15px; margin-top: auto; }
  .sachet--back .address { font-size: 6.5px; margin-top: 3px; }
</style>
</head>
<body>
  <section class="package sachet sachet--front" aria-label="Tea sachet front">
    <div class="label">
      <div class="tear-line">Please tear here</div>
      <div class="mascot mascot--blue" role="img" aria-label="Pale blue llama illustration"></div>
      <div class="brand-name">Velmora Leaf</div>
      <div class="variety-row">
        <span>Chai Tea<small>with caffeine</small></span>
        <span class="dot"></span>
        <span>Thé Chai<small>avec la caféine</small></span>
      </div>
      <h2 class="product-name">Velmora Gold</h2>
      <p class="description">An exotic blend of black tea, cardamom, fennel, cloves, ginger and cinnamon</p>
      <p class="description-fr">Un mélange exotique de thé noir, cardamome, le fenouil, clous de girofle, le gingembre et la cannelle</p>
    </div>
  </section>

  <section class="package sachet sachet--back" aria-label="Tea sachet back">
    <div class="label">
      <h3 class="heading">Directions</h3>
      <p>To get the most out of every cup bring water to boiling and steep 5 to 7 minutes depending on strength preferred.</p>
      <p>For a stronger tea, use 2 tea bags.</p>
      <p>Add milk and your choice of sweetener. Enjoy!</p>
      <p class="note">*See inside panel of box for more detailed instructions</p>
      <h3 class="heading">Ingredients</h3>
      <p class="ingredients">Black Tea, Cardamom, Cloves, Fennel, Ginger, and Cinnamon</p>
      <p class="retail">Not for individual retail sale</p>
      <div class="brand-name">Velmora Leaf</div>
      <div class="address">Box 2718 RPO Westfield<br>Lethbridge, Alberta</div>
    </div>
  </section>

  <section class="package box box--front" aria-label="Box front">
    <div class="label">
      <div class="variety-row">
        <span>Chai Tea<small>with caffeine</small></span>
        <span class="dot"></span>
        <span>Thé Chai<small>avec la caféine</small></span>
      </div>
      <h1 class="product-name">Velmora Gold</h1>
      <p class="description">An exotic blend of black tea, cardamom, fennel, cloves, ginger and cinnamon</p>
      <p class="description-fr">Un mélange exotique de thé noir, cardamome, le fenouil, clous de girofle, le gingembre et la cannelle</p>
      <div class="mascot mascot--dark" role="img" aria-label="Dark llama silhouette illustration"></div>
      <div class="brand-name">Velmora Leaf</div>
      <div class="count">18</div>
      <div class="count-label">Tea Bags<small>Sachets de thé</small></div>
      <div class="fine-print">
        No preservatives &amp; no artificial flavors
        <strong>Net Wt 54 g (1.9 oz)</strong>
        Product of Alberta, Canada
      </div>
    </div>
  </section>

  <section class="package box box--back" aria-label="Box back">
    <div class="label">
      <h2 class="heading">Directions</h2>
      <p>To get the most out of every cup, bring water to boiling and steep 5 to 7 minutes depending on strength preferred.</p>
      <p>For a stronger tea, use 2 tea bags.</p>
      <p>Add milk and your choice of sweetener. Enjoy!</p>
      <p class="note">*See inside panel of box for more detailed instructions</p>
      <h2 class="heading">Ingredients</h2>
      <p class="ingredients">Black Tea, Cardamom, Cloves, Fennel, Ginger, and Cinnamon</p>
      <div class="mascot mascot--blue" role="img" aria-label="Pale blue llama illustration"></div>
      <div class="brand-name">Velmora Leaf</div>
      <div class="address">Box 2718 RPO Westfield<br>Lethbridge, Alberta<br>Canada</div>
    </div>
  </section>
</body>
</html>
```